Need simple and modern looking business card with all my information on one side and logo on the other side
Info :
Company name - VELMAR CONSTRUCTION LLC
Company addres- 418 harbor 87th. Dunmoor park ny 10352
Email- velmarllc@tridomail.Com
Company phone number 555-318-6094
Cell number- 555-742-0583
Web site - velmarllc.Com
My name Gerald tomasino

Target Market(s)

Construction , home improvement, remodeling

Industry/Entity Type

Construction

Contact Information for Business Card

It has to be moder but at the same time simple

Font styles to use
Sans Serif

Colors
0255a3
ffffff
000000
f78f20
b1b1b1
9d9d9d
1b1b1b
33a6d7
ec1f27

Requirements
Must have
• My logo on one side maybe with a some kind of background on the other side all my information
Nice to have
• Some kind of background pictures provided by you .PLEASE HAVE ACCOUNT WITH PIXELVAULT WILL NOT PAY ANY EXTRA FEES .
Should not have
• Any kind of hamer, nails,screws, helmets itp. Please do not copy the other designs come up with something new.

```html
<!DOCTYPE html>
<html lang="en">
<head>
<meta charset="utf-8">
<title>Velmar Construction LLC – Business Card</title>
<link rel="stylesheet" href="https://fonts.googleapis.com/css2?family=Lato:wght@400;700&display=swap">
<style>
  :root {
    --stage: #2a2a2a;
    --black: #000000;
    --ink: #1b1b1b;
    --white: #ffffff;
    --orange: #f78f20;
    --blue: #0255a3;
    --sky: #33a6d7;
    --grey: #9d9d9d;
    --silver: #b1b1b1;
  }
  * { box-sizing: border-box; margin: 0; padding: 0; }
  html, body { width: 1200px; height: 900px; overflow: hidden; }
  body {
    background: var(--stage);
    font-family: "Lato", Arial, sans-serif;
    position: relative;
  }
  .card {
    position: absolute;
    width: 640px;
    height: 366px;
    border-radius: 3px;
    overflow: hidden;
    box-shadow: 0 14px 30px rgba(0,0,0,.45);
  }

  /* Back side: brand name only */
  .card-back {
    left: 90px; top: 70px;
    background: var(--black);
    display: flex; align-items: center; justify-content: center;
  }
  .back-brand {
    color: var(--white);
    font-weight: 700;
    font-size: 40px;
    letter-spacing: 6px;
    text-align: center;
    line-height: 1.25;
  }

  /* Front side: information */
  .card-front { left: 470px; top: 464px; background: var(--black); }
  .front-shapes { position: absolute; inset: 0; }

  .front-brand {
    position: absolute;
    left: 150px; top: 34px;
    color: var(--ink);
    font-weight: 700;
    line-height: 1;
  }
  .front-brand .brand-main { display: block; font-size: 62px; letter-spacing: 4px; }
  .front-brand .brand-sub { display: block; font-size: 19px; letter-spacing: 3.6px; margin-top: 6px; }

  .holder-name {
    position: absolute;
    left: 34px; top: 196px;
    font-size: 21px;
    font-weight: 700;
    letter-spacing: 1.5px;
    color: var(--orange);
  }
  .holder-name .surname { color: var(--blue); }

  .address {
    position: absolute;
    left: 34px; top: 262px;
    width: 300px;
    color: var(--white);
    font-size: 16px;
    line-height: 1.45;
    text-align: right;
  }

  .contacts {
    position: absolute;
    left: 400px; top: 176px;
    list-style: none;
    color: var(--white);
    font-size: 15px;
  }
  .contacts li { display: flex; align-items: center; gap: 10px; height: 25px; }
  .contacts svg { width: 13px; height: 13px; flex: none; }
</style>
</head>
<body>

  <section class="card card-back" aria-label="Business card back">
    <p class="back-brand">VELMAR<br>CONSTRUCTION LLC</p>
  </section>

  <section class="card card-front" aria-label="Business card front">
    <svg class="front-shapes" viewBox="0 0 640 366" width="640" height="366" aria-hidden="true">
      <rect x="0" y="0" width="640" height="150" fill="#ffffff"/>
      <rect x="0" y="150" width="350" height="84" fill="#ffffff"/>
      <line x1="350" y1="150" x2="640" y2="150" stroke="#0255a3" stroke-width="2"/>
      <line x1="0" y1="240" x2="350" y2="240" stroke="#ffffff" stroke-width="1.5"/>
    </svg>

    <p class="front-brand">
      <span class="brand-main">VELMAR</span>
      <span class="brand-sub">CONSTRUCTION LLC</span>
    </p>

    <p class="holder-name">GERALD <span class="surname">TOMASINO</span></p>

    <p class="address">418 harbor 87th.<br>Dunmoor park ny 10352</p>

    <ul class="contacts">
      <li>
        <svg viewBox="0 0 16 16" aria-hidden="true"><path d="M3 1l3 3-2 2c1 2 4 5 6 6l2-2 3 3-2 2C7 15 1 9 1 3z" fill="#0255a3"/></svg>
        555-318-6094
      </li>
      <li>
        <svg viewBox="0 0 16 16" aria-hidden="true"><rect x="4" y="1" width="8" height="14" rx="1.5" fill="none" stroke="#0255a3" stroke-width="1.8"/><rect x="7" y="12" width="2" height="1.5" fill="#0255a3"/></svg>
        555-742-0583
      </li>
      <li>
        <svg viewBox="0 0 16 16" aria-hidden="true"><rect x="1" y="3" width="14" height="10" fill="none" stroke="#0255a3" stroke-width="1.6"/><path d="M1 3l7 6 7-6" fill="none" stroke="#0255a3" stroke-width="1.6"/></svg>
        velmarllc@tridomail.com
      </li>
      <li>
        <svg viewBox="0 0 16 16" aria-hidden="true"><circle cx="8" cy="8" r="6.5" fill="none" stroke="#0255a3" stroke-width="1.5"/><ellipse cx="8" cy="8" rx="3" ry="6.5" fill="none" stroke="#0255a3" stroke-width="1.2"/><line x1="1.5" y1="8" x2="14.5" y2="8" stroke="#0255a3" stroke-width="1.2"/></svg>
        www.velmarllc.com
      </li>
    </ul>
  </section>

</body>
</html>
```